Business card - mobile service

O KiraTel is a mobile family safety service based on tablets and smartphones.
The business card must have:
BASIC INFO
Company Logo
Name
Position / Job Title: Co-founder
Mobile Phone Number: +55 (11) 5080 6172
Land Line: +55 (11) 9087 614352
Email Address: name@kiratel-example.com
Web Site URL: www.kiratel-example.com
PROMOTIONAL INFO
Try KiraTel free Today!
Your personal promo code: xxxx-2222-uuuu-7777-1234
Promo code text explanation with the instructions about the trial offer
Updates
Dears,
One more must have: the KiraTel slogan:
Industry/Entity Type
Safety
Look and feel
Each slider illustrates characteristics of the customer's brand and the style your logo design should communicate.

```html
<!DOCTYPE html>
<html lang="en">
<head>
<meta charset="utf-8">
<title>KiraTel business card</title>
<link rel="stylesheet" href="https://fonts.googleapis.com/css2?family=Open+Sans:wght@300;400;600;700&display=swap">
<style>
  :root {
    --page-bg: #ffffff;
    --card-white: #ffffff;
    --brand-blue: #14a6e6;
    --sky-blue: #05a6ee;
    --sky-glow: #5cc8f5;
    --accent-orange: #f5b400;
    --ink-dark: #0b2233;
    --ink-white: #ffffff;
  }
  * { margin: 0; padding: 0; box-sizing: border-box; }
  html, body {
    width: 1200px;
    height: 900px;
    overflow: hidden;
    background: var(--page-bg);
    font-family: "Open Sans", sans-serif;
  }
  .card {
    position: absolute;
    left: 86px;
    top: 164px;
    width: 1028px;
    height: 570px;
    background: var(--card-white);
    overflow: hidden;
  }
  .card-header {
    position: absolute;
    left: 0; top: 0;
    width: 100%;
    height: 176px;
    background: var(--card-white);
    border-bottom: 4px solid var(--accent-orange);
  }
  .brand {
    position: absolute;
    left: 46px;
    top: 36px;
    display: flex;
    align-items: center;
    gap: 14px;
  }
  .brand-name {
    font-size: 76px;
    font-weight: 700;
    color: var(--brand-blue);
    letter-spacing: -1px;
    line-height: 1;
  }
  .brand-dot {
    width: 30px;
    height: 30px;
    border-radius: 50%;
    background: var(--accent-orange);
  }
  .slogan {
    position: absolute;
    left: 50px;
    top: 124px;
    font-size: 18px;
    font-weight: 600;
    color: var(--accent-orange);
  }
  .person {
    position: absolute;
    right: 44px;
    top: 46px;
    text-align: right;
  }
  .person-name {
    font-size: 56px;
    font-weight: 700;
    color: var(--brand-blue);
    line-height: 1.05;
  }
  .person-role {
    font-size: 26px;
    font-weight: 700;
    color: var(--accent-orange);
    line-height: 1.1;
  }
  .card-body {
    position: absolute;
    left: 0; top: 180px;
    width: 100%;
    height: 390px;
    background: var(--sky-blue);
  }
  .body-glow {
    position: absolute;
    inset: 0;
    background: radial-gradient(ellipse 520px 320px at 52% 40%, var(--sky-glow) 0%, rgba(92,200,245,0) 100%);
  }
  .promo {
    position: absolute;
    left: 40px;
    top: 34px;
    width: 340px;
    color: var(--ink-white);
  }
  .promo-title {
    font-size: 24px;
    font-weight: 700;
    line-height: 1.2;
  }
  .promo-label {
    margin-top: 18px;
    font-size: 16px;
    color: var(--ink-dark);
  }
  .promo-code {
    margin-top: 4px;
    font-size: 19px;
    font-weight: 700;
    letter-spacing: 0.5px;
  }
  .promo-note {
    margin-top: 14px;
    font-size: 15px;
    line-height: 1.45;
    color: var(--ink-dark);
  }
  .contacts {
    position: absolute;
    left: 404px;
    right: 44px;
    top: 14px;
  }
  .contact-row {
    display: flex;
    justify-content: space-between;
    align-items: baseline;
    height: 66px;
    padding-top: 4px;
  }
  .contact-label {
    font-size: 21px;
    color: var(--ink-dark);
  }
  .contact-value {
    font-size: 40px;
    color: var(--ink-white);
  }
  .contact-value.is-email { font-size: 32px; }
  .website {
    position: absolute;
    right: 44px;
    top: 280px;
    font-size: 46px;
    font-weight: 300;
    letter-spacing: 1px;
    color: var(--ink-dark);
  }
</style>
</head>
<body>
  <div class="card">
    <header class="card-header">
      <div class="brand">
        <span class="brand-name">kiratel</span>
        <span class="brand-dot"></span>
      </div>
      <div class="slogan">Family safety, always close.</div>
      <div class="person">
        <div class="person-name">Ana Reis</div>
        <div class="person-role">Co-founder</div>
      </div>
    </header>
    <section class="card-body">
      <div class="body-glow" role="img" aria-label="Soft halftone dot texture on a blue background"></div>
      <div class="promo">
        <div class="promo-title">Try KiraTel free Today!</div>
        <div class="promo-label">Your personal promo code:</div>
        <div class="promo-code">xxxx-2222-uuuu-7777-1234</div>
        <p class="promo-note">Enter this code in the KiraTel app on your smartphone or tablet to start your free family safety trial.</p>
      </div>
      <div class="contacts">
        <div class="contact-row">
          <span class="contact-label">Mobile Phone:</span>
          <span class="contact-value">+55 (11) 5080 6172</span>
        </div>
        <div class="contact-row">
          <span class="contact-label">Land Line:</span>
          <span class="contact-value">+55 (11) 9087 614352</span>
        </div>
        <div class="contact-row">
          <span class="contact-label">Email:</span>
          <span class="contact-value is-email">ana.reis@kiratel-example.com</span>
        </div>
      </div>
      <div class="website">www.kiratel-example.com</div>
    </section>
  </div>
</body>
</html>
```